Small chamber of commerce in upstate new york. Need basic design to announce a new chocolate festival that will intend to bring in tourists to our area and give our local merchants exposure.

Industry/Entity Type

Chamber Of Commerce

Requirements
Must have
• (Beyond the information that has been listed on the enclosed jpeg, I would like to have some details on the reverse side that would include:)

Cooking with Chocolate Demo
Chocolate Decorating competition with Kids/Pastry Chefs
Live Music
Fudge Rocket Scooter Sprint
Lots & Lots of Chocolate!!!

More information contact info@pinevalechamber.org or call 845.555.0147.

```html
<!DOCTYPE html>
<html lang="en">
<head>
<meta charset="utf-8">
<title>Pine Vale &amp; the Chocolate Festival — Postcard</title>
<link rel="stylesheet" href="https://fonts.googleapis.com/css2?family=Stint+Ultra+Condensed&family=Julee&display=swap">
<style>
  :root {
    --page: #ffffff;
    --cocoa: #3d3629;
    --sky: #8ccbe8;
    --cream: #f4efe6;
    --rule: #4a4a4a;
    --cut: #111111;
  }
  * { box-sizing: border-box; margin: 0; padding: 0; }
  html, body { width: 1200px; height: 1200px; overflow: hidden; background: var(--page); }
  .canvas { position: relative; width: 1200px; height: 1200px; }

  .postcard { position: absolute; left: 310px; width: 574px; height: 447px; border: 1px solid var(--cut); overflow: hidden; }
  .postcard--front { top: 80px; background: var(--cocoa); }
  .postcard--back { top: 595px; background: var(--page); }

  .back-panel { position: absolute; inset: 0; background: var(--cocoa);
    clip-path: polygon(0 0, 432px 0, 432px 145px, 277px 145px, 277px 368px, 72px 368px, 72px 447px, 0 447px); }

  .swirls { position: absolute; inset: 0; width: 100%; height: 100%; }

  .eyebrow, .date, .web, .activities, .contact { font-family: "Stint Ultra Condensed", "Arial Narrow", serif; color: var(--cream); text-align: center; position: absolute; white-space: nowrap; }

  .headline { position: absolute; text-align: center; font-weight: 400; }
  .headline span { display: block; font-family: "Julee", cursive; color: var(--sky); line-height: .95; white-space: nowrap; }

  /* front */
  .front .eyebrow { left: 0; width: 572px; top: 34px; font-size: 30px; letter-spacing: 1px; }
  .front .headline { left: 0; width: 572px; top: 82px; }
  .front .the { font-size: 78px; transform: translateX(-100px); }
  .front .word-1 { font-size: 112px; transform: translateX(-8px); }
  .front .word-2 { font-size: 112px; transform: translateX(62px); }
  .front .date { left: 0; width: 572px; top: 362px; font-size: 32px; letter-spacing: 1px; }
  .front .web { left: 0; width: 572px; top: 404px; font-size: 17px; letter-spacing: .5px; }

  /* back */
  .back .eyebrow { left: 10px; width: 256px; top: 24px; font-size: 19px; }
  .back .headline { left: 10px; width: 256px; top: 46px; }
  .back .the { font-size: 38px; transform: translateX(-50px); }
  .back .word-1 { font-size: 54px; transform: translateX(-4px); }
  .back .word-2 { font-size: 54px; transform: translateX(32px); }
  .back .activities { left: 10px; width: 256px; top: 196px; list-style: none; font-size: 16px; line-height: 20px; }
  .back .contact { left: 10px; width: 256px; top: 322px; font-size: 11px; line-height: 18px; }

  .stamp { position: absolute; left: 466px; top: 30px; width: 71px; height: 98px; border: 1px solid var(--rule); }
  .address-line { position: absolute; left: 305px; width: 233px; height: 0; border-top: 1px solid var(--rule); }
</style>
</head>
<body>
<main class="canvas">

  <section class="postcard postcard--front front" aria-label="Postcard front">
    <svg class="swirls" viewBox="0 0 574 447" role="img" aria-label="Loose hand-drawn chocolate scribble swirls scattered in the corners">
      <defs>
        <radialGradient id="swirlGlow">
          <stop offset="0" stop-color="#8a4a1f" stop-opacity=".45"/>
          <stop offset="1" stop-color="#8a4a1f" stop-opacity="0"/>
        </radialGradient>
      </defs>
      <ellipse cx="60" cy="75" rx="60" ry="60" fill="url(#swirlGlow)"/>
      <ellipse cx="400" cy="40" rx="50" ry="42" fill="url(#swirlGlow)"/>
      <ellipse cx="535" cy="185" rx="55" ry="55" fill="url(#swirlGlow)"/>
      <ellipse cx="70" cy="300" rx="75" ry="65" fill="url(#swirlGlow)"/>
      <ellipse cx="525" cy="345" rx="55" ry="80" fill="url(#swirlGlow)"/>
    </svg>
    <p class="eyebrow">Pine Vale &amp;</p>
    <h1 class="headline">
      <span class="the">the</span>
      <span class="word-1">Chocolate</span>
      <span class="word-2">Festival</span>
    </h1>
    <p class="date">coming Nov 1st, 2014</p>
    <p class="web">www.pinevalechamber.org</p>
  </section>

  <section class="postcard postcard--back back" aria-label="Postcard back">
    <div class="back-panel">
      <svg class="swirls" viewBox="0 0 574 447" role="img" aria-label="Loose hand-drawn chocolate scribble swirls">
        <defs>
          <radialGradient id="swirlGlowBack">
            <stop offset="0" stop-color="#8a4a1f" stop-opacity=".45"/>
            <stop offset="1" stop-color="#8a4a1f" stop-opacity="0"/>
          </radialGradient>
        </defs>
        <ellipse cx="40" cy="45" rx="45" ry="45" fill="url(#swirlGlowBack)"/>
        <ellipse cx="340" cy="40" rx="60" ry="45" fill="url(#swirlGlowBack)"/>
        <ellipse cx="280" cy="110" rx="40" ry="60" fill="url(#swirlGlowBack)"/>
        <ellipse cx="35" cy="380" rx="45" ry="65" fill="url(#swirlGlowBack)"/>
      </svg>
      <p class="eyebrow">Pine Vale &amp;</p>
      <h2 class="headline">
        <span class="the">the</span>
        <span class="word-1">Chocolate</span>
        <span class="word-2">Festival</span>
      </h2>
      <ul class="activities">
        <li>Cooking with Chocolate Demo</li>
        <li>Chocolate Decorating competition</li>
        <li>with Kids/Pastry Chefs</li>
        <li>Live Music</li>
        <li>Fudge Rocket Scooter Sprint</li>
        <li>Lots &amp; Lots of Chocolate!!!</li>
      </ul>
      <p class="contact">More information contact info@pinevalechamber.org<br>or call 845.555.0147</p>
    </div>
    <svg class="swirls" viewBox="0 0 574 447" role="img" aria-label="Faint cream scribble swirl behind the address lines">
      <defs>
        <radialGradient id="swirlFaint">
          <stop offset="0" stop-color="#e9dfd3" stop-opacity=".8"/>
          <stop offset="1" stop-color="#e9dfd3" stop-opacity="0"/>
        </radialGradient>
      </defs>
      <ellipse cx="500" cy="340" rx="75" ry="85" fill="url(#swirlFaint)"/>
    </svg>
    <div class="stamp" aria-label="Stamp box"></div>
    <div class="address-line" style="top:193px"></div>
    <div class="address-line" style="top:228px"></div>
    <div class="address-line" style="top:263px"></div>
    <div class="address-line" style="top:298px"></div>
    <div class="address-line" style="top:332px"></div>
  </section>

</main>
</body>
</html>
```